Wine Bottle Label

Project: New Label for Marlow Wine

Sponsored by: Tall Oak Cellars (talloakcellars.example and Castellane Wines, producer of Marlow Wines)

Product Description:

Wine comes in both red (cabernet, zinfandel) and white (Chardonnay, Sauvignon Blanc). It is marketed to restaurants and mid priced retailers including Harbor Pantry, etc.) Wine is priced between $17 - $20 per bottle. The wine is in the medium price category and is intended for mid market appeal.

_
Label Requirements:

• Noticeable among other labels when on a black bottle. White labels are most noticeable but all color choices are an option if the brand stands out and can be easily recognizable from 10 – 12ft.

• Has to appeal to Gen X - younger people. Contemporary. Must appeal to women who buy the majority of wine in the US.

• Has to be presentable at the dinner table...slightly sophisticated.

• Has to connect with the “Official Bird of the Fenwick Nature League” Great White Marlow

• Bird is most often seen in grassy green pasture/meadows or wading in shallow water. Alone or in group.

• Has to fit on the bottle: Label size: 3 ½” H – 2 ¾” W

• Keep it Simple, lots of empty space

• Could be free form graphic design, illustrations, photos, etc.

• Could be abstract representation providing it connects to Egrets, e.g. stamp of foot which is gold embossed or similar.)

• Label must contain:

o Brand Name: Marlow
o Varietal: will vary (Cabernet Sauvignon, Chardonnay, Sauvignon Blanc, Zinfandel, etc.)
o Appellation: varies (Sonoma County, Napa Valley, California)
o Vintage: 2010, 2011, etc.

• Variations in label color/design are possible between varietals but brand should be consistent.

Back design must also be included. Example of current back with text is attached.

Requirements
Must have
• Must have relationship with Marlow Bird - figuratively or literally
Has to fit on the bottle: Label size: 3 ½” H – 2 ¾” W
o Brand Name: Marlow

```html
<!DOCTYPE html>
<html lang="en">
<head>
<meta charset="utf-8">
<title>Marlow Wine — Sonoma County Sauvignon Blanc Labels</title>
<link rel="stylesheet" href="https://fonts.googleapis.com/css2?family=Jost:wght@200;300;400;500&family=Archivo+Narrow:wght@400;700&display=swap">
<style>
  :root {
    --paper: #ffffff;
    --ink: #111111;
    --soft-ink: #3a3a3a;
    --muted: #8a8a8a;
    --rule: #1a1a1a;
    --heron-blue: #6fd5ea;
    --heron-pale: #d9f5fb;
    --shadow: rgba(0, 0, 0, 0.28);
  }
  * { box-sizing: border-box; margin: 0; padding: 0; }
  html, body { width: 1200px; height: 900px; overflow: hidden; background: var(--paper); }
  .canvas { position: relative; width: 1200px; height: 900px; background: var(--paper); font-family: "Jost", sans-serif; color: var(--ink); }

  /* ---------- Front label ---------- */
  .front-label {
    position: absolute; left: 640px; top: 58px; width: 455px; height: 757px;
    background: var(--paper);
    box-shadow: 2px 6px 14px var(--shadow);
  }
  .front-label .brand-name {
    position: absolute; left: 0; right: 0; top: 40px;
    text-align: center; font-weight: 300; font-size: 76px; letter-spacing: 2px; line-height: 1;
  }
  .front-label .brand-rule {
    position: absolute; left: 105px; width: 245px; top: 126px; height: 1.5px; background: var(--rule);
  }
  .front-label .emblem { position: absolute; left: 30px; top: 190px; width: 410px; height: 290px; }
  .front-label .appellation,
  .front-label .varietal {
    position: absolute; left: 0; right: 0; text-align: center; font-weight: 200; font-size: 33px; line-height: 1;
  }
  .front-label .appellation { top: 543px; }
  .front-label .divider { position: absolute; left: 105px; width: 245px; top: 583px; height: 1.5px; background: var(--rule); }
  .front-label .varietal { top: 592px; }
  .front-label .vintage {
    position: absolute; left: 0; right: 0; top: 662px;
    display: flex; justify-content: center; align-items: center; gap: 38px;
    font-weight: 200; font-size: 42px; line-height: 1;
  }
  .front-label .vintage .mark { width: 12px; height: 12px; background: var(--ink); transform: rotate(45deg); }
  .front-label .volume,
  .front-label .abv { position: absolute; right: 12px; text-align: right; color: var(--muted); font-weight: 300; line-height: 1; }
  .front-label .volume { top: 710px; font-size: 16px; }
  .front-label .abv { top: 732px; font-size: 14px; }

  /* ---------- Back label ---------- */
  .back-label {
    position: absolute; left: 90px; top: 170px; width: 400px; height: 560px;
    background: var(--paper);
    box-shadow: 2px 6px 14px var(--shadow);
    padding: 26px 30px 20px;
    font-family: "Archivo Narrow", sans-serif; color: var(--soft-ink);
  }
  .back-label .corner { position: absolute; width: 0; height: 0; }
  .back-label .corner.top-left { left: 0; top: 0; border-top: 16px solid var(--ink); border-right: 16px solid transparent; }
  .back-label .corner.top-right { right: 0; top: 0; border-top: 16px solid var(--ink); border-left: 16px solid transparent; }
  .back-label .corner.bottom-left { left: 0; bottom: 0; border-bottom: 16px solid var(--ink); border-right: 16px solid transparent; }
  .back-label .corner.bottom-right { right: 0; bottom: 0; border-bottom: 16px solid var(--ink); border-left: 16px solid transparent; }
  .back-label .brand-name {
    font-family: "Jost", sans-serif; font-weight: 300; font-size: 34px; text-align: center; color: var(--ink); line-height: 1;
  }
  .back-label .brand-rule { width: 140px; height: 1px; background: var(--rule); margin: 8px auto 12px; }
  .back-label .wine-line {
    display: flex; justify-content: space-between; align-items: center;
    font-family: "Jost", sans-serif; font-weight: 300; font-size: 17px; color: var(--ink); margin-bottom: 10px;
  }
  .back-label .wine-line .mark { width: 8px; height: 8px; background: var(--heron-blue); transform: rotate(45deg); }
  .back-label .story { font-size: 11.5px; line-height: 1.32; margin-bottom: 9px; }
  .back-label .bottler {
    font-family: "Jost", sans-serif; font-weight: 400; font-size: 12px; letter-spacing: 0.3px;
    display: flex; align-items: center; gap: 8px; padding-top: 8px; border-top: 1px solid #cfcfcf;
  }
  .back-label .bottler .mark { width: 5px; height: 5px; background: var(--soft-ink); transform: rotate(45deg); }
  .back-label .signature { width: 150px; height: 30px; margin: 10px 0 2px; background: linear-gradient(90deg, #e8e8e8, #f5f5f5); border-radius: 3px; }
  .back-label .vintner { font-size: 10px; font-style: normal; font-weight: 700; margin-left: 30px; margin-bottom: 10px; }
  .back-label .sulfites { text-align: center; font-size: 10px; letter-spacing: 0.5px; margin-bottom: 4px; }
  .back-label .warning { font-size: 10.5px; line-height: 1.32; text-transform: uppercase; }
  .back-label .warning strong { font-weight: 700; color: var(--ink); }
  .back-label .footer {
    position: absolute; left: 30px; right: 30px; bottom: 22px;
    display: flex; justify-content: space-between; font-size: 10.5px; font-weight: 700; color: var(--ink);
  }
</style>
</head>
<body>
<main class="canvas">

  <section class="back-label" aria-label="Back label">
    <span class="corner top-left"></span>
    <span class="corner top-right"></span>
    <span class="corner bottom-left"></span>
    <span class="corner bottom-right"></span>

    <h2 class="brand-name">Marlow</h2>
    <div class="brand-rule"></div>

    <div class="wine-line"><span>Sauvignon Blanc</span><span class="mark"></span><span>Sonoma County</span></div>

    <p class="story">This wine honors the Great Marlow. These magnificent birds were hunted to near extinction in North America during the late 1800s and early 1900s for their pure white plumes. Populations have recovered since they have been protected by law. The Great Marlow is now the symbol of the Fenwick Nature League.</p>
    <p class="story">This wine was aged for 10 months in French oak barrels. The grapes for this fine crisp-style wine were harvested from several exceptional vineyards in Northern California. Please enjoy our wine and we welcome your comments at (800) 555-0142 or marlowwine.example.</p>

    <p class="bottler"><span>BOTTLED BY CASTELLANE WINERY</span><span class="mark"></span><span>SONOMA, CA</span></p>
    <div class="signature" role="img" aria-label="Handwritten vintner signature"></div>
    <p class="vintner">Peter Alden, Vintner</p>

    <p class="sulfites">CONTAINS SULFITES</p>
    <p class="warning"><strong>Government Warning:</strong> (1) According to the Surgeon General, women should not drink alcoholic beverages during pregnancy because of the risk of birth defects. (2) Consumption of alcoholic beverages impairs your ability to drive a car or operate machinery, and may cause health problems.</p>

    <div class="footer"><span>ALC 13.5% BY VOL</span><span>750 ML</span></div>
  </section>

  <section class="front-label" aria-label="Front label">
    <h1 class="brand-name">Marlow</h1>
    <div class="brand-rule"></div>

    <svg class="emblem" viewBox="0 0 410 290" role="img" aria-label="Illustration of a great white marlow in flight, tinted pale blue, crossing a black diamond">
      <defs>
        <radialGradient id="heron-tone" cx="50%" cy="45%" r="60%">
          <stop offset="0%" stop-color="var(--heron-pale)"/>
          <stop offset="100%" stop-color="var(--heron-blue)"/>
        </radialGradient>
      </defs>
      <polygon points="172,92 272,192 172,292 72,192" fill="var(--ink)" transform="translate(0,-8)"/>
      <rect x="50" y="4" width="355" height="236" rx="110" fill="url(#heron-tone)" opacity="0.85"/>
    </svg>

    <p class="appellation">Sonoma County</p>
    <div class="divider"></div>
    <p class="varietal">Sauvignon Blanc</p>
    <p class="vintage"><span class="mark"></span><span>2010</span><span class="mark"></span></p>

    <p class="volume">750 ML</p>
    <p class="abv">ALC 13.5% BY VOL</p>
  </section>

</main>
</body>
</html>
```